VORLEN Website Design

We need a website designed for our company VORLEN. We are a luxury lifestyle club that will provide benefits and services for our members. The site should be clean & sleek, preferably using black and white (or darker colors). (example sites: brimvale.example, tusko.example)

Here is a link of a sample page I did using wix. (https://pelmundry4.sitebuild.example/mypage) This can be used to get a general idea.

Target Market(s)

Upper Middle Class in the United States

Number of Pages Required

5+ page

Font styles to use
Sans Serif
Other font styles liked:
• Arial (or other similar fonts)

Requirements
Must have
• A clean design that is eye-catching and speaks to our company.
Nice to have
• Ideas for copy.

```html
<!DOCTYPE html>
<html lang="en">
<head>
<meta charset="utf-8">
<title>VORLEN — A Members Only Lifestyle Club</title>
<link rel="stylesheet" href="https://fonts.googleapis.com/css2?family=Lato:wght@300;400;700&display=swap">
<style>
  :root {
    --black: #000000;
    --ink: #111111;
    --white: #ffffff;
    --muted: #cfcfcf;
    --grey-text: #555555;
    --accent: #c9d61c;
    --line: #e2e2e2;
  }
  * { box-sizing: border-box; margin: 0; padding: 0; }
  html, body { width: 1200px; height: 2900px; overflow: hidden; }
  body {
    background: var(--white);
    font-family: "Lato", Arial, sans-serif;
    color: var(--white);
    position: relative;
  }

  /* Hero */
  .hero {
    position: absolute; left: 0; top: 0; width: 1200px; height: 660px;
    background: radial-gradient(ellipse at 30% 40%, #3c3c3c 0%, #1d1d1d 45%, #0b0b0b 100%);
  }
  .hero-photo { position: absolute; inset: 0; }
  .site-nav {
    position: absolute; left: 0; top: 0; width: 1200px; height: 120px;
    display: flex; align-items: center; justify-content: space-between;
    padding: 0 70px 0 70px;
  }
  .brand { font-size: 30px; font-weight: 400; letter-spacing: 2px; color: var(--white); }
  .nav-links { display: flex; gap: 10px; list-style: none; }
  .nav-links li {
    font-size: 15px; font-weight: 700; letter-spacing: 0.5px;
    padding: 10px 14px; text-transform: uppercase;
  }
  .nav-links .is-current { background: rgba(255,255,255,0.12); color: #9a9a9a; font-weight: 400; }
  .hero-title {
    position: absolute; left: 0; top: 245px; width: 1200px; text-align: center;
    font-size: 44px; font-weight: 400; letter-spacing: 0.5px;
  }
  .btn {
    display: inline-block; font-size: 15px; font-weight: 700; letter-spacing: 1px;
    text-transform: uppercase; color: var(--white);
  }
  .btn-accent {
    position: absolute; left: 450px; top: 350px; width: 300px; height: 56px;
    border: 2px solid var(--accent); color: var(--accent);
    display: flex; align-items: center; justify-content: center;
  }

  /* Feature rows */
  .feature {
    position: absolute; left: 0; width: 1200px; height: 600px;
    background: var(--black);
  }
  .feature-photo { position: absolute; top: 0; width: 600px; height: 600px; }
  .feature-photo.left { left: 0; }
  .feature-photo.right { left: 600px; }
  .feature-copy { position: absolute; top: 0; width: 600px; height: 600px; padding: 0 90px 0 90px; display: flex; flex-direction: column; justify-content: center; }
  .feature-copy.right { left: 600px; }
  .feature-copy.left { left: 0; padding-left: 120px; padding-right: 80px; }
  .feature-heading {
    font-size: 27px; font-weight: 400; letter-spacing: 1px; text-transform: uppercase;
    border-left: 4px solid var(--accent); padding-left: 16px; line-height: 40px;
    margin-left: -20px; margin-bottom: 34px;
  }
  .feature-text { font-size: 19px; line-height: 29px; color: var(--white); margin-bottom: 24px; }
  .btn-outline {
    margin-top: 14px; width: 208px; height: 56px; border: 2px solid var(--white);
    display: flex; align-items: center; justify-content: center;
  }

  /* Newsletter */
  .newsletter {
    position: absolute; left: 0; top: 2460px; width: 1200px; height: 340px;
    background: var(--white); color: var(--ink); text-align: center;
  }
  .newsletter-title { position: absolute; left: 0; top: 98px; width: 1200px; font-size: 35px; font-weight: 400; }
  .newsletter-lede { position: absolute; left: 0; top: 162px; width: 1200px; font-size: 18px; color: var(--grey-text); }
  .signup {
    position: absolute; left: 300px; top: 232px; width: 600px; height: 58px; display: flex; gap: 24px;
  }
  .signup-field {
    width: 416px; height: 58px; border: 2px solid var(--ink); padding: 0 22px;
    display: flex; align-items: center; font-size: 15px; color: #333;
  }
  .signup-button {
    width: 160px; height: 58px; background: var(--black); color: var(--white);
    display: flex; align-items: center; justify-content: center;
    font-size: 16px; font-weight: 700; letter-spacing: 1px;
  }

  /* Footer */
  .site-footer {
    position: absolute; left: 0; top: 2800px; width: 1200px; height: 100px;
    border-top: 1px solid var(--line); background: var(--white);
    display: flex; align-items: center; justify-content: space-between; padding: 0 50px;
  }
  .copyright { font-size: 13px; color: var(--grey-text); }
  .social { display: flex; gap: 26px; list-style: none; }
  .social li { width: 20px; height: 20px; border-radius: 50%; background: var(--ink); }
</style>
</head>
<body>

<header class="hero">
  <svg class="hero-photo" width="1200" height="660" role="img" aria-label="Dark monochrome photo of smiling friends relaxing together outdoors">
    <defs>
      <linearGradient id="heroShade" x1="0" y1="0" x2="1" y2="1">
        <stop offset="0" stop-color="#2a2a2a"/>
        <stop offset="0.5" stop-color="#3a3a3a"/>
        <stop offset="1" stop-color="#141414"/>
      </linearGradient>
    </defs>
    <rect width="1200" height="660" fill="url(#heroShade)" opacity="0.85"/>
    <rect width="1200" height="660" fill="#000" opacity="0.35"/>
  </svg>
  <nav class="site-nav">
    <div class="brand">VORLEN</div>
    <ul class="nav-links">
      <li class="is-current">Home</li>
      <li>About</li>
      <li>Services and Benefits</li>
      <li>Contact</li>
    </ul>
  </nav>
  <h1 class="hero-title">A Members Only Lifestyle Club</h1>
  <span class="btn btn-accent">Become a Member</span>
</header>

<section class="feature" style="top:660px">
  <svg class="feature-photo left" width="600" height="600" role="img" aria-label="Black and white photo of a young woman crouching on a city street">
    <defs>
      <linearGradient id="aboutShade" x1="0" y1="0" x2="0" y2="1">
        <stop offset="0" stop-color="#d9d9d9"/>
        <stop offset="0.55" stop-color="#8a8a8a"/>
        <stop offset="1" stop-color="#3a3a3a"/>
      </linearGradient>
    </defs>
    <rect width="600" height="600" fill="url(#aboutShade)"/>
  </svg>
  <div class="feature-copy right">
    <h2 class="feature-heading">About VORLEN</h2>
    <p class="feature-text">VORLEN is a members only lifestyle club founded in order to bring the best services, experiences, and opportunities to our diverse community of members.</p>
    <p class="feature-text">Our members consist of creatives, athletes, artists, and other professionals.</p>
    <span class="btn btn-outline">Learn More</span>
  </div>
</section>

<section class="feature" style="top:1260px">
  <div class="feature-copy left">
    <h2 class="feature-heading">Benefits and Services</h2>
    <p class="feature-text">VORLEN membership provides you with amazing benefits and services. Members receive access to the best accountants, attorneys, real estate agents, private bankers/advisors and more.</p>
    <p class="feature-text">VORLEN members also receive access to private flight travel, premium luxury gym membership, private social clubs, and private investment opportunities.</p>
    <span class="btn btn-outline">Learn More</span>
  </div>
  <svg class="feature-photo right" width="600" height="600" role="img" aria-label="Black and white photo of a traveller overlooking a coastal cliffside village">
    <defs>
      <linearGradient id="benefitShade" x1="0" y1="0" x2="1" y2="1">
        <stop offset="0" stop-color="#bdbdbd"/>
        <stop offset="0.5" stop-color="#8c8c8c"/>
        <stop offset="1" stop-color="#4a4a4a"/>
      </linearGradient>
    </defs>
    <rect width="600" height="600" fill="url(#benefitShade)"/>
  </svg>
</section>

<section class="feature" style="top:1860px">
  <svg class="feature-photo left" width="600" height="600" role="img" aria-label="Black and white photo of a crowd at a concert with stage lights">
    <defs>
      <radialGradient id="eventShade" cx="0.35" cy="0.3" r="0.8">
        <stop offset="0" stop-color="#cfcfcf"/>
        <stop offset="0.45" stop-color="#5a5a5a"/>
        <stop offset="1" stop-color="#111111"/>
      </radialGradient>
    </defs>
    <rect width="600" height="600" fill="url(#eventShade)"/>
  </svg>
  <div class="feature-copy right">
    <h2 class="feature-heading">Experiences</h2>
    <p class="feature-text">VORLEN organizes and supports a ton of private events and parties for our members who are also provided access to exclusive venues and events from our partners.</p>
    <p class="feature-text">Network with other members to build lasting relationships.</p>
    <span class="btn btn-outline">Learn More</span>
  </div>
</section>

<section class="newsletter">
  <h2 class="newsletter-title">Subscribe To Our Newletter</h2>
  <p class="newsletter-lede">Sign up today to our weekly news, hot deals &amp; exclusive events to stay up to date!</p>
  <div class="signup">
    <div class="signup-field">Enter Your Email Address</div>
    <div class="signup-button">SIGN UP</div>
  </div>
</section>

<footer class="site-footer">
  <p class="copyright">© 2018 by Ashfield Taper Co. All rights reserved.</p>
  <ul class="social" aria-label="Social links">
    <li></li><li></li><li></li><li></li><li></li>
  </ul>
</footer>

</body>
</html>
```